Fore Sale sign for my real estate agency

I am a Brisbane - Australia inner western suburbs boutique real estate agent who is needing a for sale sign. We are a small dynamic family agency that needs a for sale sign that will standout and give us a strong presence in the market.

I have attached a logo I like, however I am not fixed on anything and am open to suggestions.

The information on the sign should contain but not necessarily limited to the following information - please appreciate I am very open
1 logo - Vellman
2 Ph number - 3847 1593
3 web address - vellman.example.au

Thank you
Glen Vellman

```html
<!DOCTYPE html>
<html lang="en">
<head>
<meta charset="utf-8">
<title>Vellman – For Sale Sign</title>
<link href="https://fonts.googleapis.com/css2?family=Open+Sans:wght@700;800&display=swap" rel="stylesheet">
<style>
  :root {
    --stage: #e9eaec;
    --strip: #38363a;
    --strip-text: #5c5a60;
    --orange: #e8582a;
    --orange-deep: #cf4a20;
    --orange-light: #f06a35;
    --white: #ffffff;
  }
  html, body {
    margin: 0;
    padding: 0;
    width: 1200px;
    height: 1000px;
    overflow: hidden;
    background: var(--stage);
    font-family: "Open Sans", Arial, sans-serif;
  }
  .sign {
    position: absolute;
    left: 284px;
    top: 80px;
    width: 632px;
    height: 840px;
    background: var(--orange);
    box-shadow: 0 10px 30px rgba(0,0,0,0.18);
    overflow: hidden;
  }
  .sign__field {
    position: absolute;
    left: 152px;
    top: 0;
    width: 480px;
    height: 840px;
    background: linear-gradient(155deg, var(--orange-deep) 0%, var(--orange-light) 35%, var(--orange) 60%, var(--orange-deep) 85%, var(--orange-light) 100%);
  }
  .sign__strip {
    position: absolute;
    left: 0;
    top: 0;
    width: 152px;
    height: 840px;
    background: var(--strip);
  }
  .sign__strip-name {
    position: absolute;
    left: 28px;
    top: 16px;
    writing-mode: vertical-rl;
    transform: rotate(180deg);
    font-weight: 700;
    font-size: 84px;
    line-height: 96px;
    color: var(--strip-text);
    letter-spacing: 1px;
  }
  .sign__headline {
    position: absolute;
    right: 63px;
    top: 108px;
    margin: 0;
    text-align: right;
    font-weight: 700;
    font-size: 176px;
    line-height: 188px;
    letter-spacing: -3px;
    color: var(--white);
    text-shadow: 0 4px 10px rgba(0,0,0,0.25);
  }
  .sign__contact {
    position: absolute;
    right: 66px;
    top: 556px;
    text-align: right;
    color: var(--white);
    font-weight: 700;
  }
  .sign__phone {
    font-size: 34px;
    line-height: 56px;
  }
  .sign__web {
    font-size: 26px;
    line-height: 56px;
  }
  .sign__brand {
    position: absolute;
    right: 63px;
    top: 690px;
    font-weight: 700;
    font-size: 70px;
    line-height: 90px;
    color: var(--white);
    letter-spacing: 1px;
  }
</style>
</head>
<body>
  <div class="sign">
    <div class="sign__field" role="img" aria-label="Orange faceted low-poly triangle background"></div>
    <div class="sign__strip">
      <div class="sign__strip-name">Vellman</div>
    </div>
    <h1 class="sign__headline">FOR<br>SALE</h1>
    <div class="sign__contact">
      <div class="sign__phone">07 3847 1593</div>
      <div class="sign__web">www.vellman.example.au</div>
    </div>
    <div class="sign__brand">Vellman</div>
  </div>
</body>
</html>
```